Relaunch website https://dancepastdawn.de/

We are looking for creative minds to relaunch the website for our new musical “Dance past dawn” (www.dancepastdawn.de). The aim is to convey the full emotional power, spine-tingling intensity, and spirit of empowerment of this unique production.

The site should make the emotional depth and power of the musical come to life - not merely by describing it, but by letting people feel it. In accordance with our marketing philosophy: "Show, don't tell"—we tell the story, rather than simply promoting the musical.

The website should be responsive, offer intuitive navigation and be in accordance with the design guidelines. Please design the website with the compatibility of a specific our website platform theme in mind (in the best case choose from a big enterprise theme such as avada, enfold or divi).

Design specifications:
Primary color: Pink (R224 / G51 / B151)
Secondary color: yellow (R255 / G221 / B0)
Tertiary color: black (R29 / G29 / B27)
Font-Headline: Tungsten
Font body: DIN 1451 LT Pro
Background texture: Grunge

In addition to the main page, the following subpages will be relevant:
OURtale, The Musical, Cast & Team, Tickets, Plan your visit, Corporate events, Press, FAQ, Coupon, News

The winner will be selected according to the following criteria: creativity, user guidance, technical feasibility and compliance with the style guide. Also based on your unique ideas! We know the briefing is super specific but please let your ideas and feedback flow.

We have uploaded a detailed briefing document (including the CI) in German and English as well as the logos. You can use all available graphics from the current website and socials if needed for your pitch. Please design at least the following pages:
- Home (briefing included)
- OURTale (be creative - no specific briefing)
- Ticketing (separate briefing included)
- Corporate events (separate briefing included)
- Plan your visit (separate briefing included)
- News (be creative - no specific briefing)

If you have any questions, please contact marla.fenwick@dosuvel-entertainment.

We would love to give you more time for your designs!

Target Market(s)

Germany

Industry/Entity Type

Musical & Entertainment

Number of Pages Required

5+ page

Font styles to use
Other font styles liked:
• Headline: Tungsten & Body: DIN 1451 LT Pro

Colors
FFF300
FFF600
FEFA6F
FFFEC7
FFFEE8
E54698
E96AAD
F1A4CE
F9D9EA
FCEFF6

Requirements
Must have
• See briefing
Nice to have
• See briefing
Should not have
• See briefing

```html
<!DOCTYPE html>
<html lang="en">
<head>
<meta charset="utf-8">
<title>Dance past dawn – Das Musical</title>
<link rel="stylesheet" href="https://fonts.googleapis.com/css2?family=Anton&family=Barlow:wght@400;600;700&display=swap">
<style>
:root{
  --pink:#e03397;
  --yellow:#ffdd00;
  --black:#1d1d1b;
  --ink:#0e0e0d;
  --cream:#f6f1ea;
  --white:#ffffff;
  --stage:#8e8e8e;
}
*{box-sizing:border-box;margin:0;padding:0}
html,body{width:1200px;height:4454px;overflow:hidden}
body{background:var(--stage);font-family:'Barlow',Arial,sans-serif;color:var(--white)}
.page{position:absolute;left:81px;top:83px;width:1037px;height:4286px;overflow:hidden;background:var(--black)}
.display{font-family:'Anton',Impact,sans-serif;font-weight:400;text-transform:uppercase;line-height:.98;letter-spacing:.5px}
.kicker{font-family:'Barlow',Arial,sans-serif;font-weight:700;font-size:9px;letter-spacing:1.6px;text-transform:uppercase}
.btn{display:inline-block;font-family:'Barlow',Arial,sans-serif;font-weight:700;font-size:9px;letter-spacing:.8px;text-transform:uppercase;padding:9px 14px}
.btn-yellow{background:var(--yellow);color:var(--black);box-shadow:4px 4px 0 var(--black)}
.btn-outline{border:1.5px solid var(--white);color:var(--white)}
section{position:absolute;left:0;width:1037px}
.col{position:absolute}

/* announcement */
.announce{position:absolute;left:0;top:0;width:1037px;height:17px;background:var(--yellow);color:var(--black);font-size:7px;font-weight:700;letter-spacing:.8px;text-align:center;line-height:17px;text-transform:uppercase}

/* hero */
.hero{top:17px;height:661px;background:radial-gradient(ellipse at 50% 30%,#b1285f 0%,#8f2051 45%,#5e1636 100%)}
.hero::before{content:"";position:absolute;left:0;top:0;width:100%;height:90px;background:linear-gradient(#25161b,rgba(37,22,27,0))}
.nav{position:absolute;left:48px;right:40px;top:14px;height:30px;display:flex;align-items:center;justify-content:space-between}
.wordmark{font-family:'Anton',Impact,sans-serif;font-size:18px;color:var(--white);text-transform:uppercase;letter-spacing:.3px}
.nav ul{display:flex;gap:16px;list-style:none;align-items:center;font-size:7.5px;font-weight:700;letter-spacing:.6px;text-transform:uppercase}
.nav .btn{font-size:7.5px;padding:7px 10px;box-shadow:3px 3px 0 var(--pink)}
.ghost-mark{position:absolute;left:316px;top:165px;width:436px;height:314px;background:rgba(224,51,151,.25);border:1px solid rgba(255,221,0,.12)}
.brand-box{position:absolute;left:379px;top:61px;width:280px;height:185px;background:var(--pink);text-align:center;padding-top:12px}
.brand-box .over{font-size:7px;font-weight:700;letter-spacing:1px;color:var(--white);text-transform:uppercase}
.brand-box .name{font-family:'Anton',Impact,sans-serif;font-size:58px;line-height:.95;color:var(--yellow);text-transform:uppercase;margin-top:6px}
.brand-box .sub{font-size:9px;font-weight:700;letter-spacing:5px;color:var(--white);text-transform:uppercase;margin-top:4px}
.hero-copy{position:absolute;left:0;width:100%;top:268px;text-align:center}
.hero-copy .kicker{color:var(--white);font-size:7px}
.hero .hero-title{font-size:74px;line-height:.93;color:var(--yellow);margin-top:8px;text-shadow:4px 4px 0 var(--pink)}
.hero .hero-sub{font-size:34px;color:var(--white);margin-top:6px;line-height:1}
.hero-sub span{color:var(--yellow)}
.hero-actions{margin-top:14px;display:flex;gap:14px;justify-content:center}
.scroll-cue{margin-top:16px;font-size:6.5px;font-weight:700;letter-spacing:1.2px;text-transform:uppercase}

/* forgotten */
.forgotten{top:678px;height:418px;background:var(--black)}
.forgotten .kicker{color:var(--yellow);font-size:7px}
.forgotten h2{font-size:52px;margin-top:10px;color:var(--white)}
.forgotten .intro{font-size:10px;line-height:1.6;color:var(--white)}
.forgotten .facts{font-size:44px;color:var(--yellow);margin-top:16px;line-height:.97}
.link{font-size:7px;font-weight:700;letter-spacing:.8px;text-transform:uppercase;color:var(--yellow);margin-top:14px}

/* heart */
.heart{top:1096px;height:528px;background:var(--pink)}
.portrait{position:absolute;left:200px;top:140px;width:299px;height:247px;background:var(--yellow);box-shadow:10px 10px 0 var(--black);text-align:center}
.portrait .ball{position:absolute;left:126px;top:34px;width:46px;height:46px;border-radius:50%;background:var(--white);border:2px solid var(--black)}
.portrait .label{position:absolute;left:0;right:0;bottom:26px;font-size:42px;color:var(--black)}
.heart .kicker{color:var(--white)}
.heart h2{font-size:52px;margin-top:10px;color:var(--white)}
.heart .body{font-size:10px;line-height:1.6;margin-top:12px}
.heart .quote{font-family:'Anton',Impact,sans-serif;font-size:27px;line-height:1.05;color:var(--yellow);margin-top:20px}

/* turning point */
.turning{top:1624px;height:708px;background:var(--pink)}
.turning svg{position:absolute;left:0;top:0}
.turning .kicker{color:var(--yellow)}
.turning h2{font-size:50px;margin-top:10px;color:var(--white)}
.turning .body{font-size:10px;margin-top:10px}
.turning .slogan{font-size:56px;color:var(--yellow);margin-top:22px;text-shadow:3px 3px 0 var(--pink);line-height:1}
.closing{position:absolute;left:0;right:0;top:522px;text-align:center}
.closing h2{font-size:54px;color:var(--white);margin-top:0}
.closing .body{font-size:10px;margin-top:12px}
.closing .btn{margin-top:16px;font-size:9px;padding:11px 20px}

/* timeline */
.timeline{top:2332px;height:395px;background:var(--black)}
.timeline .kicker{color:var(--yellow);font-size:7px}
.timeline h2{font-size:54px;margin-top:10px}
.years{position:absolute;left:200px;top:208px;display:flex;gap:10px}
.year{width:151px;height:126px;border:1.5px solid var(--white);padding:16px 14px}
.year b{display:block;font-family:'Anton',Impact,sans-serif;font-weight:400;font-size:32px;color:var(--yellow)}
.year span{display:block;font-size:8px;line-height:1.5;margin-top:12px}
.year.is-key{background:var(--pink);border-color:var(--pink)}

/* tickets */
.tickets{top:2727px;height:463px;background:var(--cream);color:var(--black)}
.tickets .kicker,.news .kicker{color:var(--pink);font-size:7px}
.tickets h2{font-size:54px;margin-top:10px}
.tickets .lead{font-size:8.5px;margin-top:12px}
.cards{position:absolute;left:200px;top:279px;display:flex;gap:11px}
.card{width:204px;height:128px;background:var(--white);padding:14px 16px;box-shadow:5px 5px 0 var(--pink)}
.card h3{font-family:'Anton',Impact,sans-serif;font-weight:400;font-size:17px;text-transform:uppercase}
.card p{font-size:7.5px;line-height:1.5;margin-top:6px}
.card .btn{font-size:7px;padding:6px 8px;margin-top:14px;box-shadow:none}
.card.is-featured{background:var(--pink);color:var(--white);box-shadow:5px 5px 0 var(--yellow)}

/* visit */
.visit{top:3190px;height:294px;background:var(--yellow);color:var(--black)}
.visit h2{font-size:52px}
.visit .addr{font-size:8px;margin-top:14px}
.visit h3{font-family:'Anton',Impact,sans-serif;font-weight:400;font-size:17px;text-transform:uppercase}
.visit .col p.detail{font-size:8px;margin-top:10px}

/* corporate */
.corporate{top:3484px;height:337px;background:var(--black)}
.corporate .kicker{color:var(--yellow);font-size:7px}
.corporate h2{font-size:54px;margin-top:10px}
.corporate .body{font-size:8px;line-height:1.6;margin-top:12px}
.enquiry{position:absolute;left:595px;top:73px;width:240px;height:199px;background:var(--pink);padding:14px 14px;box-shadow:8px 8px 0 var(--yellow)}
.field{background:var(--white);height:26px;margin-bottom:8px;font-size:7px;color:#777;padding:8px 8px}
.field.tall{height:62px}
.enquiry .btn{display:block;text-align:center;box-shadow:none;font-size:7.5px;padding:8px}

/* news */
.news{top:3821px;height:375px;background:var(--cream);color:var(--black)}
.news h2{font-size:54px;margin-top:10px}
.posts{position:absolute;left:200px;top:207px;display:flex;gap:11px}
.post{width:204px;height:107px;background:var(--white);border:1.5px solid var(--black);padding:16px 14px;box-shadow:5px 5px 0 var(--yellow)}
.post small{display:block;font-size:6.5px;font-weight:700;color:var(--pink);letter-spacing:.8px;text-transform:uppercase}
.post h3{font-family:'Anton',Impact,sans-serif;font-weight:400;font-size:17px;line-height:1;text-transform:uppercase;margin-top:4px}

/* footer */
.footer{position:absolute;left:0;width:1037px;top:4196px;height:90px;background:var(--ink)}
.footer .wordmark{position:absolute;left:48px;top:34px;font-size:22px}
.footer .meta{position:absolute;left:820px;top:26px;font-size:7px;line-height:2.2}
.footer .meta b{font-weight:700}
</style>
</head>
<body>
<main class="page">

  <div class="announce">World premiere Cologne 2026 • Inspired by a true story • Limited tickets coming soon •</div>

  <section class="hero">
    <nav class="nav">
      <span class="wordmark">Dance past dawn</span>
      <ul>
        <li>OURtale</li><li>The Musical</li><li>Tickets</li><li>Plan Visit</li><li>Corporate</li><li>News</li>
        <li><span class="btn btn-yellow">Get Tickets</span></li>
      </ul>
    </nav>
    <div class="ghost-mark" role="img" aria-label="Faint enlarged title backdrop in grunge texture"></div>
    <div class="brand-box">
      <div class="over">Nach einer wahren Geschichte</div>
      <div class="name">Dance<br>past dawn</div>
      <div class="sub">Das Musical</div>
    </div>
    <div class="hero-copy">
      <div class="kicker">Inspired by a true story</div>
      <h1 class="display hero-title">A team<br>nobody<br>believed in.</h1>
      <p class="display hero-sub">It's not history. It's<br><span>OURtale.</span></p>
      <div class="hero-actions">
        <span class="btn btn-yellow">Get Tickets</span>
        <span class="btn btn-outline">Discover the story</span>
      </div>
      <div class="scroll-cue">Scroll to feel the story</div>
    </div>
  </section>

  <section class="forgotten">
    <div class="col" style="left:200px;top:69px;width:300px">
      <div class="kicker">1981 — Inspired by true events</div>
      <h2 class="display">Forgotten<br>stories<br>that<br>change the<br>world.</h2>
    </div>
    <div class="col" style="left:536px;top:72px;width:300px">
      <p class="intro">An invitation arrives from Taiwan. The dream is huge. The support is missing. A team of women refuses to disappear quietly.</p>
      <p class="display facts">Nine games.<br>Eleven days.<br>Undefeated.<br>World<br>champions.</p>
      <div class="link">Open the timeline →</div>
    </div>
  </section>

  <section class="heart">
    <div class="portrait">
      <div class="ball" role="img" aria-label="Football icon"></div>
      <div class="display label">Lotte</div>
    </div>
    <div class="col" style="left:536px;top:72px;width:310px">
      <div class="kicker">At the heart of the story</div>
      <h2 class="display">From shy<br>wallflower<br>to a woman<br>who owns<br>the field.</h2>
      <p class="body">Lotte stands between family expectations, society's rules, and the one thing that makes her feel alive: football.</p>
      <p class="quote">“Some dreams don't ask permission.”</p>
    </div>
  </section>

  <section class="turning">
    <svg width="1037" height="463" viewBox="0 0 1037 463" aria-hidden="true">
      <polygon points="0,0 719,0 259,463 0,463" fill="#1d1d1b"/>
    </svg>
    <div class="col" style="left:277px;top:70px;width:600px">
      <div class="kicker">The turning point</div>
      <h2 class="display">A dream bigger<br>than any doubt.</h2>
      <p class="body">Training. Fundraising. Departure. The world says no — they answer together.</p>
      <p class="display slogan">Open doors<br>tear down walls<br>change the world</p>
    </div>
    <div class="closing">
      <h2 class="display">Dance past dawn</h2>
      <p class="body">A story that must be told. A musical that gets under your skin. From November 2026 in Cologne.</p>
      <span class="btn btn-yellow">Get your tickets now</span>
    </div>
  </section>

  <section class="timeline">
    <div class="col" style="left:200px;top:66px;width:640px">
      <div class="kicker">The true story</div>
      <h2 class="display">From prohibition to<br>world champions.</h2>
    </div>
    <div class="years">
      <div class="year"><b>1955</b><span>Women's football is banned by the federation.</span></div>
      <div class="year"><b>1970</b><span>The ban is lifted, but equality is still far away.</span></div>
      <div class="year is-key"><b>1981</b><span>The Miracle of Taipei: courage becomes history.</span></div>
      <div class="year"><b>2026</b><span>The story arrives as a world premiere in Cologne.</span></div>
    </div>
  </section>

  <section class="tickets">
    <div class="col" style="left:200px;top:66px;width:640px">
      <div class="kicker">Ticket information</div>
      <h2 class="display">Choose your<br>seat. Bring your<br>team.</h2>
      <p class="lead">Clear ticket categories, group discounts, social tickets, and booking integration prepared for our website platform.</p>
    </div>
    <div class="cards">
      <div class="card"><h3>Single Tickets</h3><p>For visitors who want the full emotional live experience.</p><span class="btn btn-yellow">Book now</span></div>
      <div class="card is-featured"><h3>Groups</h3><p>Tiered discounts for friends, teams, clubs, and school groups.</p><span class="btn btn-yellow">Ask for group offer</span></div>
      <div class="card"><h3>Social Tickets</h3><p>Cultural access for everyone, with accessible ticket options.</p><span class="btn btn-yellow">Learn more</span></div>
    </div>
  </section>

  <section class="visit">
    <div class="col" style="left:200px;top:58px;width:220px">
      <h2 class="display">Plan<br>your<br>visit</h2>
      <p class="addr">Hall Nine at Brennwerk, Cologne-Nord.</p>
    </div>
    <div class="col" style="left:444px;top:60px;width:190px">
      <h3>Arrive</h3><p class="detail">Tram, bus, parking, and local route details.</p>
    </div>
    <div class="col" style="left:652px;top:60px;width:200px">
      <h3>Enjoy</h3><p class="detail">Restaurants, hotels, dinner + show packages.</p>
    </div>
  </section>

  <section class="corporate">
    <div class="col" style="left:200px;top:66px;width:370px">
      <div class="kicker">Corporate events</div>
      <h2 class="display">Business<br>meets<br>empowerment.</h2>
      <p class="body">Team-building events, VIP packages, corporate evenings, and group experiences around a story of courage and solidarity.</p>
    </div>
    <form class="enquiry">
      <div class="field">Company name</div>
      <div class="field">Email address</div>
      <div class="field tall">Tell us about your event</div>
      <span class="btn btn-yellow">Request package</span>
    </form>
  </section>

  <section class="news">
    <div class="col" style="left:200px;top:66px;width:640px">
      <div class="kicker">News</div>
      <h2 class="display">Behind the<br>scenes</h2>
    </div>
    <div class="posts">
      <article class="post"><small>Update</small><h3>World premiere preparations begin in Cologne.</h3></article>
      <article class="post"><small>Interview</small><h3>The women behind the story that refused to fade.</h3></article>
      <article class="post"><small>Press</small><h3>Download center and media contact area.</h3></article>
    </div>
  </section>

  <footer class="footer">
    <span class="wordmark">Dance past dawn</span>
    <div class="meta"><b>Become part of the movement.</b><br>Newsletter • Social Media • Press • FAQ • Gift Vouchers</div>
  </footer>

</main>
</body>
</html>
```